We are training college name LEARNORIVA looking for Logo,flyer,Brochure and email [url removed, login to view] courses are: 1. Diploma of Business
2. Diploma of Marketing
[url removed, login to view] of Leadership Management
[url removed, login to view] Diploma of Business
[url removed, login to view] Diploma of Marketing
[url removed, login to view] Diploma of Leadership Management
[url removed, login to view] II in Hospitality
Work requirement:
-Design must be related to Academic
-Modern western

```html
<!DOCTYPE html>
<html lang="en">
<head>
<meta charset="utf-8">
<title>Learnoriva – Course Flyer</title>
<link href="https://fonts.googleapis.com/css2?family=Fjalla+One&family=Cinzel:wght@400&display=swap" rel="stylesheet">
<style>
  :root {
    --backdrop: #d4d4d4;
    --paper: #ffffff;
    --mustard: #e5b34f;
    --lime: #c9dc72;
    --ink-light: #ffffff;
    --bullet: #2f4a52;
    --brand-brown: #8a6a4f;
    --photo-top: rgba(229, 179, 79, 0);
    --photo-mid: #9c8148;
    --photo-bottom: #4f4536;
    --coral: #d65a55;
  }
  * { margin: 0; padding: 0; box-sizing: border-box; }
  html, body {
    width: 1142px;
    height: 1200px;
    overflow: hidden;
    background: var(--backdrop);
  }
  .flyer {
    position: absolute;
    left: 171px;
    top: 30px;
    width: 800px;
    height: 1140px;
    background: var(--mustard);
    overflow: hidden;
  }
  .flyer-header {
    position: absolute;
    left: 0; top: 0;
    width: 100%;
    height: 268px;
    background: var(--paper);
    display: flex;
    align-items: center;
    justify-content: center;
  }
  .brand {
    display: flex;
    align-items: center;
    gap: 14px;
    font-family: "Cinzel", serif;
    font-size: 34px;
    letter-spacing: 1px;
    color: var(--brand-brown);
    margin-top: 40px;
  }
  .brand-dot {
    width: 16px; height: 16px;
    border-radius: 50%;
    background: var(--brand-brown);
  }
  .header-notch {
    position: absolute;
    left: 382px;
    top: 266px;
    width: 44px;
    height: 22px;
  }
  .programs {
    position: absolute;
    left: 241px;
    top: 330px;
  }
  .programs-title {
    font-family: "Fjalla One", sans-serif;
    font-size: 58px;
    font-weight: 400;
    color: var(--lime);
    line-height: 1;
    margin-bottom: 26px;
  }
  .course-list { list-style: none; }
  .course-list li {
    position: relative;
    font-family: "Fjalla One", sans-serif;
    font-size: 19px;
    color: var(--ink-light);
    height: 52px;
    line-height: 24px;
    padding-left: 25px;
  }
  .course-list li svg {
    position: absolute;
    left: 0; top: 7px;
    width: 10px; height: 10px;
  }
  .graduates-photo {
    position: absolute;
    left: 0;
    top: 676px;
    width: 100%;
    height: 434px;
    background: linear-gradient(to bottom, var(--photo-top) 0%, var(--photo-mid) 45%, var(--photo-bottom) 100%);
  }
  .footer-band {
    position: absolute;
    left: 0; bottom: 0;
    width: 100%;
    height: 30px;
    background: var(--coral);
  }
</style>
</head>
<body>
  <main class="flyer">
    <header class="flyer-header">
      <div class="brand"><span class="brand-dot"></span>LEARNORIVA</div>
    </header>
    <svg class="header-notch" viewBox="0 0 44 22" aria-hidden="true">
      <polygon points="0,0 44,0 22,22" fill="var(--paper)"/>
    </svg>

    <section class="programs">
      <h1 class="programs-title">Learnoriva</h1>
      <ul class="course-list">
        <li><svg viewBox="0 0 10 10"><polygon points="0,0 10,0 0,10" fill="var(--bullet)"/></svg>Diploma of Business</li>
        <li><svg viewBox="0 0 10 10"><polygon points="0,0 10,0 0,10" fill="var(--bullet)"/></svg>Diploma of Marketing</li>
        <li><svg viewBox="0 0 10 10"><polygon points="0,0 10,0 0,10" fill="var(--bullet)"/></svg>Diploma of Leadership Management</li>
        <li><svg viewBox="0 0 10 10"><polygon points="0,0 10,0 0,10" fill="var(--bullet)"/></svg>Advance Diploma of Business</li>
        <li><svg viewBox="0 0 10 10"><polygon points="0,0 10,0 0,10" fill="var(--bullet)"/></svg>Advance Diploma of Marketing</li>
        <li><svg viewBox="0 0 10 10"><polygon points="0,0 10,0 0,10" fill="var(--bullet)"/></svg>Advance Diploma of Leadership Management</li>
        <li><svg viewBox="0 0 10 10"><polygon points="0,0 10,0 0,10" fill="var(--bullet)"/></svg>Certificate II in Hospitality</li>
      </ul>
    </section>

    <div class="graduates-photo" role="img" aria-label="Photo of cheering graduates in black gowns raising their arms"></div>
    <div class="footer-band"></div>
  </main>
</body>
</html>
```